Business Card Design Project

Need a business card designed for a horse racing/gambling centered company.
Company name is BrightQuill.com.au
Company colours are similar to those in the logo.
Something clean and modern , designer given liberty to be creative.
Incorporate the logo is preferred.
Single or Double Sided fine
Must include :
Name
Mobile Number
Email Address
Reason: Apologies, I have been traveling unexpectedly with business and just need the extra two days to reply and give feedback before making a decision.
Industry/Entity Type
Business

```html
<!DOCTYPE html>
<html lang="en">
<head>
<meta charset="utf-8">
<title>BrightQuill business card</title>
<link rel="stylesheet" href="https://fonts.googleapis.com/css2?family=Yanone+Kaffeesatz:wght@300;400;500&display=swap">
<style>
  :root {
    --stage: #e6e8ea;
    --card-light: #f1f1f1;
    --card-mid: #d9d9d9;
    --teal: #1a9a94;
    --teal-dark: #12756f;
    --bar: #8a8a8a;
    --bar-text: #f4f4f4;
    --ink: #3d3d3d;
    --faint: rgba(120,120,120,0.18);
  }
  * { box-sizing: border-box; margin: 0; padding: 0; }
  html, body { width: 1068px; height: 1200px; overflow: hidden; }
  body {
    background: var(--stage);
    font-family: "Yanone Kaffeesatz", "Arial Narrow", sans-serif;
    position: relative;
  }
  .card {
    position: absolute;
    left: 94px;
    width: 880px;
    height: 500px;
    background: linear-gradient(135deg, var(--card-light) 0%, var(--card-mid) 55%, var(--card-light) 100%);
    box-shadow: 0 6px 18px rgba(0,0,0,0.18);
    overflow: hidden;
  }
  .card--front { top: 60px; }
  .card--back { top: 640px; }

  /* faint brand mark on the front */
  .brand-ghost {
    position: absolute;
    left: 50px; top: 70px;
    width: 350px; height: 350px;
    border-radius: 50%;
    border: 14px solid var(--faint);
    display: flex; align-items: center; justify-content: center;
  }
  .brand-ghost__name {
    font-size: 50px; font-weight: 400;
    color: var(--faint);
    letter-spacing: 1px;
  }

  /* contact bars */
  .contact-list {
    position: absolute;
    left: 420px; top: 55px; right: 0;
    list-style: none;
  }
  .contact-list__item {
    position: relative;
    height: 26px;
    margin-bottom: 8px;
    background: var(--bar);
    border-bottom: 3px solid #c7c7c7;
    padding-left: 60px;
    font-size: 19px; font-weight: 300;
    line-height: 25px;
    color: var(--bar-text);
  }
  .contact-list__flag {
    position: absolute; left: 0; top: 0;
  }
  .contact-list__item--link { color: #cfe9e7; }

  /* name block */
  .identity {
    position: absolute;
    left: 450px; top: 300px;
    width: 360px;
    text-align: center;
  }
  .identity__company {
    font-size: 30px; font-weight: 400;
    color: #fafafa;
    text-shadow: 0 1px 1px rgba(0,0,0,0.25);
    letter-spacing: 1px;
  }
  .identity__rule { height: 3px; background: var(--teal); }
  .identity__name {
    font-size: 44px; font-weight: 400;
    color: var(--ink);
    line-height: 46px;
    margin: 2px 0;
  }
  .identity__position {
    font-size: 24px; font-weight: 500;
    color: #333;
    margin-top: 2px;
  }

  /* back brand lockup */
  .brand-lockup {
    position: absolute;
    left: 50%; top: 50%;
    transform: translate(-50%, -50%);
    display: flex; align-items: center; gap: 16px;
  }
  .brand-lockup__dot {
    width: 46px; height: 46px; border-radius: 50%;
    background: var(--teal);
  }
  .brand-lockup__name {
    font-size: 52px; font-weight: 500;
    color: var(--teal-dark);
  }
</style>
</head>
<body>
  <section class="card card--front">
    <div class="brand-ghost"><span class="brand-ghost__name">BrightQuill.com.au</span></div>

    <ul class="contact-list">
      <li class="contact-list__item">
        <svg class="contact-list__flag" width="44" height="26" viewBox="0 0 44 26"><polygon points="0,0 44,0 44,26 0,26 12,13" fill="#1a9a94"/></svg>
        1207 /52 Harbour Lane, Sydney, NSW , 2000
      </li>
      <li class="contact-list__item">
        <svg class="contact-list__flag" width="44" height="26" viewBox="0 0 44 26"><polygon points="0,0 44,0 44,26 0,26 12,13" fill="#1a9a94"/></svg>
        Phone: 0400555017
      </li>
      <li class="contact-list__item contact-list__item--link">
        <svg class="contact-list__flag" width="44" height="26" viewBox="0 0 44 26"><polygon points="0,0 44,0 44,26 0,26 12,13" fill="#1a9a94"/></svg>
        peter@brightquill.com.au
      </li>
      <li class="contact-list__item contact-list__item--link">
        <svg class="contact-list__flag" width="44" height="26" viewBox="0 0 44 26"><polygon points="0,0 44,0 44,26 0,26 12,13" fill="#1a9a94"/></svg>
        www.brightquill.com.au
      </li>
    </ul>

    <div class="identity">
      <div class="identity__company">BRIGHTQUILL</div>
      <div class="identity__rule"></div>
      <div class="identity__name">PETER HOLLIS</div>
      <div class="identity__rule"></div>
      <div class="identity__position">position</div>
    </div>
  </section>

  <section class="card card--back">
    <div class="brand-lockup">
      <span class="brand-lockup__dot"></span>
      <span class="brand-lockup__name">BrightQuill.com.au</span>
    </div>
  </section>
</body>
</html>
```